Word template Letterhead for Australian Law Firm

We are a small law firm based in Manly, NSW, Australia. We have had a new logo designed for us and wish to freshen up the appearance of our letterhead. We require the letterhead to be in a word document that we can type over. This will not be a ‘printed’ letterhead because we send the majority of our correspondence via email. We would like to see a few options. We have attached our previous letterhead as well as the artwork for our new logo. We like the idea of a watermark across the bottom of the letter but the watermark must stay in place and we must be able to type over it. We are open to some colour throughout the letterhead because the majority of our correspondence is sent electronically. We also use electronic signatures. I have uploaded an example of this.The letterhead must include:-1. Our address details – including our phone number, physical address, website address etc. These details can be found on the copy of our previous letterhead;2. ABN Number;3. The words ‘Corvenda (NSW) Pty Ltd ACN 742 185 903 trading as Shipton & AssociatesLiability limited by a scheme approved under Professional Standards Legislation. The letterhead does not need to include the names and qualifications of the people working at the firm. Thank you.

Target Market(s)

Clients and other parties

Industry/Entity Type

Law Firm

Font styles to use
Other font styles liked:
• raleway, montserrat

Colors

Designer to choose colors to be used in the design.

Requirements
Must have
• Certain wording - please see project description.
• Must be a word document and must be able to type over the watermark etc.
Nice to have
• Watermark at the bottom of the letter.

```html
<!DOCTYPE html>
<html lang="en">
<head>
<meta charset="utf-8">
<title>Ferrow &amp; Associates Letterhead</title>
<link href="https://fonts.googleapis.com/css2?family=Open+Sans:wght@400;600;700&display=swap" rel="stylesheet">
<style>
  :root {
    --backdrop: #ededee;
    --paper: #fbfbfb;
    --ink: #3c3c40;
    --ink-soft: #5a5a60;
    --navy: #2f3c8f;
    --gold: #b9a377;
    --wave-blue: #dfe3ef;
    --wave-gold: #efeadd;
    --rule: #9a9aa2;
  }
  * { box-sizing: border-box; margin: 0; padding: 0; }
  html, body { width: 1200px; height: 795px; overflow: hidden; }
  body {
    background: var(--backdrop);
    font-family: "Open Sans", Arial, sans-serif;
    color: var(--ink);
    position: relative;
  }
  .letterhead {
    position: absolute;
    left: 331px; top: 15px;
    width: 538px; height: 765px;
    background: var(--paper);
    box-shadow: 0 2px 10px rgba(0,0,0,0.12);
    overflow: hidden;
  }
  .watermark {
    position: absolute;
    left: 150px; bottom: 0;
    width: 388px; height: 330px;
    background: radial-gradient(ellipse at 70% 80%, var(--wave-gold) 0%, rgba(239,234,221,0) 55%),
                radial-gradient(ellipse at 35% 60%, var(--wave-blue) 0%, rgba(223,227,239,0) 60%);
    opacity: 0.8;
  }
  .brand {
    position: absolute;
    left: 52px; top: 58px;
    display: flex; align-items: center; gap: 8px;
  }
  .brand-dot {
    width: 22px; height: 22px; border-radius: 50%;
    background: var(--navy);
  }
  .brand-name {
    font-size: 12px; font-weight: 600; color: var(--navy);
    letter-spacing: 0.2px;
  }
  .contact {
    position: absolute;
    left: 352px; top: 52px;
    padding-left: 8px;
    border-left: 1px solid var(--rule);
    font-size: 6.4px; line-height: 9px; color: var(--ink-soft);
  }
  .contact li { list-style: none; display: flex; align-items: center; gap: 3px; }
  .contact svg { width: 6px; height: 6px; fill: var(--navy); }
  .salutation {
    position: absolute;
    left: 52px; top: 150px;
    font-size: 11.5px; color: var(--ink);
  }
  .body-copy {
    position: absolute;
    left: 52px; top: 178px; width: 432px;
    font-size: 7px; line-height: 10.4px; color: var(--ink-soft);
  }
  .body-copy p { margin-bottom: 10px; }
  .sign-off {
    position: absolute;
    left: 52px; top: 450px;
    font-size: 7px; color: var(--ink-soft);
  }
  .signature {
    position: absolute;
    left: 60px; top: 466px;
    width: 54px; height: 18px;
    background: linear-gradient(90deg, #e6e6ea, #d4d4da);
    border-radius: 3px;
  }
  .accreditation {
    position: absolute;
    left: 64px; top: 498px;
    width: 30px; height: 30px; border-radius: 50%;
    background: var(--navy);
  }
  .legal-footer {
    position: absolute;
    right: 40px; bottom: 36px;
    text-align: right;
    font-size: 6.6px; line-height: 9.6px; font-weight: 600; color: var(--ink-soft);
  }
</style>
</head>
<body>
  <main class="letterhead">
    <div class="watermark" role="img" aria-label="Faint brand watermark sweeping across the bottom of the page"></div>

    <header class="brand">
      <span class="brand-dot"></span>
      <span class="brand-name">Ferrow &amp; Associates</span>
    </header>

    <ul class="contact">
      <li>Suite 3, 18 Kelso Street</li>
      <li>Seabright NSW 2101</li>
      <li><svg viewBox="0 0 10 10"><path d="M2 0h2l1 3-1.5 1a6 6 0 0 0 2.5 2.5L7 5l3 1v2c0 1-1 2-2 2A8 8 0 0 1 0 2c0-1 1-2 2-2z"/></svg>(02) 9000 4817</li>
      <li><svg viewBox="0 0 10 10"><path d="M2 0h2l1 3-1.5 1a6 6 0 0 0 2.5 2.5L7 5l3 1v2c0 1-1 2-2 2A8 8 0 0 1 0 2c0-1 1-2 2-2z"/></svg>(02) 9000 4818</li>
      <li><svg viewBox="0 0 10 10"><path d="M0 2h10v6H0z M0 2l5 3.5L10 2" /></svg>reception@corvendalaw.com.au</li>
      <li><svg viewBox="0 0 10 10"><circle cx="5" cy="5" r="5"/></svg>ferrowassociates.com.au</li>
      <li>ABN 48 742 185 903</li>
    </ul>

    <h1 class="salutation" style="font-weight:400">Dear Mr. Hartley,</h1>

    <section class="body-copy">
      <p>Lorem ipsum dolor sit amet, consectetur adipiscing elit. Donec orci purus, luctus vitae dignissim eu, iaculis sed purus. Vivamus faucibus, ipsum nec aliquet viverra, leo mauris condimentum ligula, sit amet sagittis enim ligula quis arcu. Nam egestas tortor id nisl porttitor mattis. In tortor ante, ultricies in suscipit a, tempus non massa. Vivamus at auctor mi. Fusce vel massa nulla. Phasellus nec eros mauris, et scelerisque orci.</p>
      <p>Donec malesuada orci vitae nulla accumsan porta a id massa. Quisque accumsan iaculis magna sit amet fringilla. Maecenas consequat, magna eget tincidunt semper, odio nibh rutrum mi, id feugiat ante nisl eu risus. Vestibulum nunc orci, rhoncus a placerat in, ultricies in mi. Cras mattis varius eros, vel fringilla nisi suscipit eget. Quisque scelerisque sagittis nulla at porttitor.</p>
      <p>Sed id augue vitae urna euismod commodo aliquet a quam. Pellentesque arcu velit, cursus et malesuada ut, consequat et diam. Nullam erat sem, rhoncus id ullamcorper vitae, rhoncus et arcu. In ultricies ultricies nulla, ut rutrum nisi iaculis at. Donec eu magna a metus ornare faucibus. Fusce aliquet faucibus ultricies. Morbi semper, est id tincidunt gravida, sem arcu adipiscing lacus, ac bibendum nulla leo eu purus. Quisque nec diam sed risus consectetur accumsan quis quis nibh. Vestibulum id purus lorem.</p>
      <p>It is a long established fact that a reader will be distracted by the readable content of a page when looking at its layout. The point of using Lorem Ipsum is that it has a more-or-less normal distribution of letters, as opposed to using 'Content here, content here', making it look like readable English. Many desktop publishing packages.</p>
    </section>

    <p class="sign-off">Sincerely,</p>
    <div class="signature" role="img" aria-label="Electronic signature"></div>
    <div class="accreditation" role="img" aria-label="Accreditation badge"></div>

    <footer class="legal-footer">
      <p>Corvenda (NSW) Pty Ltd ACN 742 185 903 trading as Ferrow &amp; Associates</p>
      <p>Liability limited by a scheme approved under Professional Standards Legislation. Legal practitioners at</p>
      <p>Corvenda (NSW) Pty Ltd are members of the scheme.</p>
    </footer>
  </main>
</body>
</html>
```